Need a graphic design to promote our new online learning system

We are seeking a graphic design to be promoted on social media to promote our new Online earning Management system (ZOR-LMS). The purpose is to make the design attractive and informative for parents and students so they can enrol at our School.

It must state the benefits of the ZOR-LMS. Colourful but not too busy.

```html
<!DOCTYPE html>
<html lang="en">
<head>
<meta charset="utf-8">
<title>ZOR-LMS Online Learning Management System</title>
<link rel="stylesheet" href="https://fonts.googleapis.com/css2?family=Barlow:wght@300;400;800;900&display=swap">
<style>
  :root {
    --navy: #0b3f8c;
    --band: #0a4b95;
    --ink: #1c1c1c;
    --grey-text: #9a9a9a;
    --cyan: #0aa2e3;
    --sky-bottom: #f4f5f6;
  }
  * { margin: 0; padding: 0; box-sizing: border-box; }
  html, body { width: 675px; height: 1200px; overflow: hidden; }
  body { font-family: "Barlow", Arial, sans-serif; background: var(--sky-bottom); }
  .poster { position: relative; width: 675px; height: 1200px; overflow: hidden; }
  .campus-backdrop {
    position: absolute; inset: 0;
    background:
      linear-gradient(180deg, rgba(255,255,255,0) 60%, rgba(247,247,247,1) 90%),
      linear-gradient(160deg, #e4eaf0 0%, #f0f3f6 35%, #dfe5ea 55%, #eef0f2 75%, #f6f6f6 100%);
  }
  .student-cutout {
    position: absolute; left: 0; top: 0; width: 252px; height: 430px;
    background: linear-gradient(180deg, #d9c3b2 0%, #c9a48d 25%, #e5798a 50%, #8a96a8 80%, rgba(220,226,232,0) 100%);
    border-radius: 0 120px 0 0;
    opacity: .75;
  }
  .brand {
    position: absolute; left: 275px; top: 58px; width: 374px; text-align: center;
    color: var(--navy); font-weight: 400;
  }
  .brand-square {
    display: block; width: 52px; height: 60px; margin: 0 auto 22px;
    background: var(--navy);
  }
  .brand-name {
    font-size: 36px; letter-spacing: .14em; line-height: 1; text-transform: uppercase;
    padding-left: .14em;
  }
  .brand-sub {
    margin-top: 16px;
    font-size: 19px; letter-spacing: .1em; line-height: 1; text-transform: uppercase;
  }
  .headline { position: absolute; left: 0; top: 380px; width: 675px; text-align: center; }
  .headline-code {
    display: block; color: var(--navy); font-weight: 900; font-size: 52px; line-height: 56px;
  }
  .headline-main {
    display: block; color: var(--navy); font-weight: 900; font-size: 72px; line-height: 68px;
    letter-spacing: .03em; padding-left: .03em;
  }
  .headline-sub {
    display: block; margin-top: 2px; color: var(--ink); font-weight: 300; font-size: 46px;
    line-height: 48px; letter-spacing: .15em; padding-left: .15em;
  }
  .learner-photo {
    position: absolute; left: 47px; top: 571px; width: 581px; height: 301px;
    background:
      radial-gradient(ellipse at 65% 55%, #b9c6da 0%, #8a95a8 25%, rgba(60,45,35,0) 55%),
      linear-gradient(90deg, #6e5a3e 0%, #3a2e25 40%, #2b2420 70%, #5a4a3c 100%);
  }
  .benefits {
    position: absolute; left: 52px; top: 906px; width: 566px;
    font-weight: 800; font-size: 27px; line-height: 31.5px; text-transform: uppercase;
    color: var(--grey-text); letter-spacing: .01em;
  }
  .benefits-call { color: var(--cyan); }
  .footer-band { position: absolute; left: 0; top: 1144px; width: 675px; height: 56px; background: var(--band); }
</style>
</head>
<body>
<main class="poster">
  <div class="campus-backdrop" role="img" aria-label="Faded photo of modern campus buildings under a pale sky"></div>
  <div class="student-cutout" role="img" aria-label="Smiling student with a backpack carrying a tall stack of books"></div>

  <header class="brand">
    <span class="brand-square"></span>
    <div class="brand-name">International</div>
    <div class="brand-sub">Academy of Zorvale</div>
  </header>

  <h1 class="headline">
    <span class="headline-code">(ZOR-LMS)</span>
    <span class="headline-main">ONLINE EARNING</span>
    <span class="headline-sub">MANAGEMENT SYSTEM</span>
  </h1>

  <div class="learner-photo" role="img" aria-label="Student wearing headphones studying at a laptop in a warm café"></div>

  <p class="benefits">
    Learn anytime, anywhere with lessons, quizzes and live classes in one place. Parents follow grades, attendance and teacher notes in real time.
    <span class="benefits-call">Enrol today and give your child a smarter school year.</span>
  </p>

  <div class="footer-band"></div>
</main>
</body>
</html>
```